INTRODUCING - BRINDLE MOTOR CENTRE

WE WOULD LIKE TO TIDY UP OUR INTRODUCTION TO OUR COMPANY
WE NEED THE WORDING TO BE SIMILAR WITH our web page
https://brindlemotorcentre.example.nz/services/

this needs to be more concise with pictures added THAT TIE IN WITH EXPLAINATIONS

```html
<!DOCTYPE html>
<html lang="en">
<head>
<meta charset="utf-8">
<title>Brindle Motor Centre – Brake &amp; Clutch Specialist Flyer</title>
<link rel="stylesheet" href="https://fonts.googleapis.com/css2?family=Montserrat:wght@400;500;600;700;800;900&family=Open+Sans:wght@400;600;700&display=swap">
<style>
  :root{
    --yellow:#fcd800;
    --yellow-soft:#f6e15a;
    --black:#1c1c1c;
    --ink:#222222;
    --grey-band:#e6e6e6;
    --paper:#ffffff;
    --canvas:#efefef;
    --muted:#444444;
  }
  *{box-sizing:border-box;margin:0;padding:0}
  html,body{width:1200px;height:2400px;overflow:hidden;background:var(--canvas)}
  body{position:relative;font-family:"Open Sans",Arial,sans-serif;color:var(--ink)}
  .page{position:absolute;left:180px;width:840px;height:1185px;background:var(--paper);overflow:hidden;box-shadow:0 4px 14px rgba(0,0,0,.25)}
  .page--front{top:5px}
  .page--back{top:1205px}
  .abs{position:absolute}

  .brand-block{left:0;top:0;width:285px;height:202px;background:var(--yellow);display:flex;flex-direction:column;align-items:center;justify-content:center;gap:14px}
  .top-band{left:285px;top:0;width:200px;height:202px;background:var(--yellow-soft)}
  .brand-mark{width:64px;height:64px;border-radius:50%;background:var(--black)}
  .brand-name{font-family:"Montserrat",Arial,sans-serif;font-weight:700;font-size:19px;color:var(--black);letter-spacing:.3px;text-align:center;line-height:1.2}

  .hero-frame{left:0;top:0;width:840px;height:530px}

  .headline{left:38px;top:248px;font-family:"Montserrat",Arial,sans-serif;color:var(--black)}
  .headline__kicker{font-size:29px;font-weight:500;letter-spacing:.5px}
  .headline__main{font-size:72px;font-weight:900;line-height:.92;margin-top:6px;letter-spacing:1px}
  .headline__accent{color:var(--yellow)}
  .headline__tail{font-size:49px;font-weight:500;margin-top:6px;letter-spacing:1px}

  .pill{position:absolute;background:var(--yellow);border-radius:30px;font-family:"Montserrat",Arial,sans-serif;font-weight:800;color:var(--black);display:flex;align-items:center;justify-content:center;letter-spacing:.5px}
  .pill--md{height:40px;font-size:23px}

  .body-text{font-size:11.4px;line-height:1.38;color:var(--muted)}
  .body-text p + p{margin-top:11px}

  .service-icons{left:490px;top:568px;width:330px;height:120px}
  .service{position:absolute;display:flex;align-items:center;gap:10px;font-family:"Open Sans",Arial,sans-serif;font-size:24px;color:var(--ink)}
  .service__icon{width:46px;height:46px;border-radius:50%;background:var(--yellow);display:flex;align-items:center;justify-content:center}

  .section-title{font-family:"Montserrat",Arial,sans-serif;font-weight:600;font-size:22px;color:var(--black)}
  .section-title--yellow{color:var(--yellow);font-weight:800}
  .section-title--heavy{font-weight:800;font-size:24px}

  .check-list{list-style:none;font-family:"Montserrat",Arial,sans-serif;font-weight:600;font-size:16.5px;line-height:21px;color:var(--black)}
  .check-list li::before{content:"\2714";margin-right:9px;font-size:14px}

  .tick-list{list-style:none;font-family:"Open Sans",Arial,sans-serif;font-weight:600;font-size:12.5px;line-height:1.3;color:var(--ink)}
  .tick-list li{position:relative;padding-left:30px}
  .tick-list li::before{content:"";position:absolute;left:2px;top:1px;width:7px;height:12px;border-right:3px solid var(--yellow);border-bottom:3px solid var(--yellow);transform:rotate(40deg)}

  .photo{position:absolute}

  .footer{left:0;bottom:0;width:840px;height:95px}
  .footer__text{position:absolute;display:flex;align-items:center;gap:14px}
  .footer__phone{font-family:"Montserrat",Arial,sans-serif;font-weight:600;font-size:29px;color:var(--black)}
  .footer__address{font-family:"Montserrat",Arial,sans-serif;font-weight:600;font-size:15px;color:var(--black)}
  .footer__contact{font-family:"Montserrat",Arial,sans-serif;font-weight:500;font-size:15.5px;color:#fff}
  .icon-circle{width:36px;height:36px;border-radius:50%;border:2px solid #fff;display:flex;align-items:center;justify-content:center}

  .grey-band{left:0;top:0;width:840px;height:194px;background:var(--grey-band)}
  .dark-band{left:0;top:407px;width:840px;height:156px;background:var(--black)}
</style>
</head>
<body>

<section class="page page--front">
  <div class="abs top-band"></div>

  <svg class="abs hero-frame" viewBox="0 0 840 530">
    <defs>
      <linearGradient id="heroTone" x1="0" y1="0" x2="1" y2="1">
        <stop offset="0" stop-color="#6d7a5a"/>
        <stop offset=".45" stop-color="#e2c92a"/>
        <stop offset=".75" stop-color="#2a2a2a"/>
        <stop offset="1" stop-color="#555"/>
      </linearGradient>
    </defs>
    <polygon points="330,262 484,0 840,0 840,528 488,528" fill="var(--yellow)"/>
    <polygon role="img" aria-label="Photo of a yellow sports car with a black bonnet driving on a road" points="350,262 496,8 840,8 840,514 498,514" fill="url(#heroTone)"/>
  </svg>

  <div class="abs brand-block">
    <div class="brand-mark"></div>
    <div class="brand-name">BRINDLE MOTOR CENTRE</div>
  </div>

  <div class="abs headline">
    <div class="headline__kicker">NEW ZEALAND 'S</div>
    <div class="headline__main">BRAKE &amp;<br><span class="headline__accent">CLUTCH</span></div>
    <div class="headline__tail">SPECIALIST</div>
  </div>

  <div class="pill pill--md" style="left:36px;top:518px;width:186px">ABOUT US</div>
  <div class="abs body-text" style="left:40px;top:572px;width:410px">
    <p>Brindle Motor Centre is a Kingsford based company who are the specialists for hard to source cables, brake parts &amp; hoses – cars, motorbikes, trucks, agriculture &amp; industrial.</p>
    <p>Our Roadcare aproved workshop can undertake all types of vehicle repairs. Whether your vehicle is a late model a classic or a commercial Brindle can repair or manufacture parts for you.</p>
  </div>

  <div class="abs service-icons">
    <div class="service" style="left:0;top:0">
      <span class="service__icon"><svg width="26" height="26" viewBox="0 0 26 26"><path d="M3 13h14M17 9h5v8h-5z" stroke="#1c1c1c" stroke-width="3" fill="none"/></svg></span>Cables
    </div>
    <div class="service" style="left:166px;top:0">
      <span class="service__icon"><svg width="26" height="26" viewBox="0 0 26 26"><circle cx="13" cy="13" r="10" stroke="#1c1c1c" stroke-width="3" fill="none"/><circle cx="13" cy="13" r="4" fill="#1c1c1c"/></svg></span>Brakes
    </div>
    <div class="service" style="left:0;top:66px">
      <span class="service__icon"><svg width="26" height="26" viewBox="0 0 26 26"><path d="M6 4v18M20 4v18M6 13h14" stroke="#1c1c1c" stroke-width="3"/></svg></span>Parts
    </div>
    <div class="service" style="left:170px;top:70px">
      <span class="service__icon"><svg width="26" height="26" viewBox="0 0 26 26"><path d="M4 20h10a6 6 0 0 0 6-6V5" stroke="#1c1c1c" stroke-width="3" fill="none"/></svg></span>Hoses
    </div>
  </div>

  <div class="pill pill--md" style="left:36px;top:716px;width:250px">OUR SERVICES</div>
  <div class="abs section-title" style="left:38px;top:772px">CABLES</div>
  <div class="abs body-text" style="left:38px;top:806px;width:768px">
    <p>At Brindle Motor Centre we design, manufacture &amp; distribute specially engineered cables for a wide range of customers including marine, agriculture, lawn care, trucking, heavy lifting &amp; recreational vehicle. We utilise the Linkflex system in producing our push/pull cables and these cables are used throughout the world with recognised brands such as Tarrow, Holt and Skyvane.</p>
    <p>We strive to add value by listening to our customers, understanding their needs and working to provide innovative solutions. As our cables are all made on site so we are able to offer our customers a quick turnaround time. Our reputation as a supplier of premium products has been earned for over 20 years in New Zealand.</p>
  </div>

  <ul class="abs check-list" style="left:40px;top:926px">
    <li>Hand Brake</li><li>Clutch Cable</li><li>Motor Cycle</li><li>Marine</li><li>Throttle</li><li>Gear Shifter Cables</li><li>Transmission</li>
  </ul>
  <ul class="abs check-list" style="left:253px;top:926px">
    <li>Excavator</li><li>Push Pull</li><li>Agricultural</li><li>Marine</li><li>Remote Cable Controls</li><li>Speedo Cables</li>
  </ul>

  <div class="photo" role="img" aria-label="Photo of a coiled black cable roll" style="left:504px;top:914px;width:290px;height:172px;background:linear-gradient(90deg,#1e1e1e,#6a6a6a 30%,#2a2a2a 55%,#777 80%,#222)"></div>

  <svg class="abs footer" viewBox="0 0 840 95" aria-hidden="true">
    <rect width="840" height="95" fill="var(--yellow)"/>
    <polygon points="452,0 840,0 840,95 366,95" fill="var(--black)"/>
  </svg>
  <div class="footer__text" style="left:42px;top:1098px">
    <svg width="30" height="30" viewBox="0 0 24 24"><path d="M6.6 10.8a15 15 0 0 0 6.6 6.6l2.2-2.2a1 1 0 0 1 1-.25 11 11 0 0 0 3.6.6 1 1 0 0 1 1 1V20a1 1 0 0 1-1 1A17 17 0 0 1 3 4a1 1 0 0 1 1-1h3.5a1 1 0 0 1 1 1c0 1.25.2 2.450 .6 3.6a1 1 0 0 1-.25 1z" fill="#1c1c1c"/></svg>
    <span class="footer__phone">0800 55 01 23</span>
  </div>
  <div class="footer__text" style="left:44px;top:1140px">
    <svg width="26" height="30" viewBox="0 0 24 28"><path d="M12 0a9 9 0 0 0-9 9c0 7 9 19 9 19s9-12 9-19a9 9 0 0 0-9-9zm0 12.5A3.5 3.5 0 1 1 12 5.5a3.5 3.5 0 0 1 0 7z" fill="#1c1c1c"/></svg>
    <span class="footer__address">12 Harlow Rd, Eastfield, Kingsford</span>
  </div>
  <div class="footer__text" style="left:456px;top:1100px">
    <span class="icon-circle"><svg width="18" height="14" viewBox="0 0 18 14"><rect x="1" y="1" width="16" height="12" fill="none" stroke="#fff" stroke-width="1.8"/><path d="M1 1l8 7 8-7" fill="none" stroke="#fff" stroke-width="1.8"/></svg></span>
    <span class="footer__contact">parts@brindlemotorcentre.example.nz</span>
  </div>
  <div class="footer__text" style="left:456px;top:1141px">
    <span class="icon-circle"><svg width="20" height="20" viewBox="0 0 20 20"><circle cx="10" cy="10" r="8.5" fill="none" stroke="#fff" stroke-width="1.6"/><ellipse cx="10" cy="10" rx="4" ry="8.5" fill="none" stroke="#fff" stroke-width="1.4"/><path d="M1.5 10h17M3 5.5h14M3 14.5h14" stroke="#fff" stroke-width="1.4"/></svg></span>
    <span class="footer__contact" style="font-size:14px">brindlemotorcentre.example.nz/services/</span>
  </div>
</section>

<section class="page page--back">
  <div class="abs grey-band"></div>
  <div class="abs section-title section-title--heavy" style="left:40px;top:30px">BRAKES</div>
  <div class="abs body-text" style="left:42px;top:70px;width:766px">
    Brindle Motor Centre specialise in the repair of all brake components including resleeving cylinders, boosters, calipers, proportioning valves &amp; brake linings.<br>
    All our resleeving is carried out using seamless stainless steel. Brake caliper seals and pistons do require replacement overtime; if new pistons are unavailable these can also be resleeved in stainless steel.<br>
    We also rebuild Brake boosters and porportioning valves, providing all parts are available and are also capable to have products relined in brake material. Brindle Motor Centre prides it selves in ensuring a quick turnaround for all of the above services.
  </div>

  <ul class="abs tick-list" style="left:40px;top:214px;width:210px">
    <li style="margin-bottom:12px">Stainless Steel Resleeving</li>
    <li style="margin-bottom:12px">Booster Reconditioning</li>
    <li style="margin-bottom:12px">Cost Effective saving time and money</li>
    <li>All types of cylinders, pistons, booster bodies can be resleeved or repaired</li>
  </ul>
  <div class="photo" role="img" aria-label="Photo of a reconditioned brake caliper with brass fittings" style="left:262px;top:206px;width:320px;height:180px;background:radial-gradient(ellipse at 45% 60%,#8a8a8a,#b3a46a 50%,#ffffff 72%)"></div>
  <ul class="abs tick-list" style="left:602px;top:214px;width:220px">
    <li style="margin-bottom:12px">Brake Caliper Rebuilds</li>
    <li style="margin-bottom:12px">Exchange Cylinders available</li>
    <li style="margin-bottom:12px">Disc Caliper Pistons – Resleeved or Manufactured</li>
    <li>Quick turn-a-round. Most cylinders received early morning will be processed and despatched same day (subject to parts availablity)</li>
  </ul>

  <div class="abs dark-band"></div>
  <div class="abs section-title section-title--yellow" style="left:40px;top:418px">PARTS</div>
  <div class="abs body-text" style="left:42px;top:450px;width:766px;color:#eeeeee">
    Here at Brindle Motor Centre we hold an extensive range of specialised parts for all your brake requirements. We specialise in the "hard to get" parts. We can source components from overseas when needs require and are specialists in making and supplying components for brake pipes.<br>
    Apart from our reconditioning program we have access to and extensive range of parts including hydraulic cylinders, shoes, drums, rotors, pads, repair kits, etc. We cater for vehicle from 1920's to current models with that in mind with over 20 years in business we understand the needs and wants of our customers.
  </div>

  <svg class="abs" style="left:0;top:563px" width="272" height="212" viewBox="0 0 272 212">
    <defs>
      <linearGradient id="shelfTone" x1="0" y1="0" x2="1" y2="0">
        <stop offset="0" stop-color="#6b5a45"/><stop offset=".5" stop-color="#c9c2b5"/><stop offset="1" stop-color="#5c5248"/>
      </linearGradient>
    </defs>
    <polygon points="0,0 214,0 272,104 214,208 0,208" fill="var(--yellow)"/>
    <polygon role="img" aria-label="Photo of a parts warehouse with stocked shelving" points="0,0 206,0 262,104 206,204 0,204" fill="url(#shelfTone)"/>
  </svg>

  <ul class="abs tick-list" style="left:312px;top:584px;width:290px;font-size:12px;line-height:26.6px">
    <li>Flywheel Machining</li><li>Commercial Wheel Cylinders</li><li>Hydraulic Brake Kits and Seals</li><li>Brake Boosters, Kits and Seals</li><li>Brake Shoe Rebonding</li><li>Clutch Parts (new and reconditioned)</li><li>Brake Piping (Bundy tube, tube nuts etc)</li>
  </ul>
  <ul class="abs tick-list" style="left:610px;top:576px;width:220px;font-size:12px;line-height:1.3">
    <li style="margin-bottom:10px">Disc and Drum machining</li>
    <li style="margin-bottom:10px">CV Joints<br>Brake Fluid<br>(Super Heavy Duty, 500ml)</li>
    <li style="margin-bottom:10px">Cleanstop Parts Cleaner</li>
    <li style="margin-bottom:10px">Brake Hoses</li>
    <li style="margin-bottom:10px">Disc Rotors</li>
    <li style="margin-bottom:10px">Disc Pads</li>
    <li>Brake Shoes</li>
  </ul>

  <div class="pill pill--md" style="left:38px;top:790px;width:232px">BRAIDED HOSES</div>
  <div class="pill pill--md" style="left:342px;top:790px;width:178px">HOSES</div>
  <div class="abs body-text" style="left:45px;top:848px;width:252px;text-align:justify">
    To compliment our Brake and Automotive hoses, Brindle Motor Centre can offer to have your hoses made in Braid for greater endurance and better look. Brindle have a large range of hoses and fittings to make or supply to our customers needs.
  </div>
  <div class="abs body-text" style="left:342px;top:848px;width:180px;text-align:justify">
    Brindle Motor Centre have been manufacturing brake hoses for more than 15 years. The hose and end fittings that we have in stock should enable us to supply brake hoses for up to 90% of the vehicles on the road today. Most brake hoses can be made while you wait.
  </div>
  <div class="pill pill--md" style="left:38px;top:964px;width:276px">AUTOMOTIVE HOSES</div>
  <div class="abs body-text" style="left:45px;top:1026px;width:380px">
    Brindle Motor Centre make on site, Power Steering hoses, Fuel hoses, etc., for any application needed on your vehicle.
  </div>

  <svg class="abs" style="left:534px;top:832px" width="306" height="258" viewBox="0 0 306 258">
    <defs>
      <linearGradient id="benchTone" x1="0" y1="0" x2="1" y2="1">
        <stop offset="0" stop-color="#3f6e86"/><stop offset=".5" stop-color="#b48f74"/><stop offset="1" stop-color="#2f4f5f"/>
      </linearGradient>
    </defs>
    <polygon points="0,128 76,0 306,0 306,258 76,258" fill="var(--yellow)"/>
    <polygon role="img" aria-label="Photo of hands crimping a hose fitting in a workshop press" points="10,128 84,6 306,6 306,252 84,252" fill="url(#benchTone)"/>
  </svg>

  <svg class="abs footer" viewBox="0 0 840 95" aria-hidden="true">
    <rect width="840" height="95" fill="var(--yellow)"/>
    <polygon points="452,0 840,0 840,95 366,95" fill="var(--black)"/>
  </svg>
  <div class="footer__text" style="left:42px;top:1098px">
    <svg width="30" height="30" viewBox="0 0 24 24"><path d="M6.6 10.8a15 15 0 0 0 6.6 6.6l2.2-2.2a1 1 0 0 1 1-.25 11 11 0 0 0 3.6.6 1 1 0 0 1 1 1V20a1 1 0 0 1-1 1A17 17 0 0 1 3 4a1 1 0 0 1 1-1h3.5a1 1 0 0 1 1 1c0 1.25.2 2.45.6 3.6a1 1 0 0 1-.25 1z" fill="#1c1c1c"/></svg>
    <span class="footer__phone">0800 55 01 23</span>
  </div>
  <div class="footer__text" style="left:44px;top:1140px">
    <svg width="26" height="30" viewBox="0 0 24 28"><path d="M12 0a9 9 0 0 0-9 9c0 7 9 19 9 19s9-12 9-19a9 9 0 0 0-9-9zm0 12.5A3.5 3.5 0 1 1 12 5.5a3.5 3.5 0 0 1 0 7z" fill="#1c1c1c"/></svg>
    <span class="footer__address">12 Harlow Rd, Eastfield, Kingsford</span>
  </div>
  <div class="footer__text" style="left:456px;top:1100px">
    <span class="icon-circle"><svg width="18" height="14" viewBox="0 0 18 14"><rect x="1" y="1" width="16" height="12" fill="none" stroke="#fff" stroke-width="1.8"/><path d="M1 1l8 7 8-7" fill="none" stroke="#fff" stroke-width="1.8"/></svg></span>
    <span class="footer__contact">parts@brindlemotorcentre.example.nz</span>
  </div>
  <div class="footer__text" style="left:456px;top:1141px">
    <span class="icon-circle"><svg width="20" height="20" viewBox="0 0 20 20"><circle cx="10" cy="10" r="8.5" fill="none" stroke="#fff" stroke-width="1.6"/><ellipse cx="10" cy="10" rx="4" ry="8.5" fill="none" stroke="#fff" stroke-width="1.4"/><path d="M1.5 10h17M3 5.5h14M3 14.5h14" stroke="#fff" stroke-width="1.4"/></svg></span>
    <span class="footer__contact" style="font-size:14px">brindlemotorcentre.example.nz/services/</span>
  </div>
</section>

</body>
</html>
```